VKTO Meridian LLC Website

Basic website for a start up business in the defense and federal space. If we could have intelligence analysis and technology as a focus that would be great. Looking to use our core colors but a lighter set of web pages would be preferable

Target Market(s)

Defense

Coding

Coded - Design and coding required

Number of Pages Required

3 page

```html
<!DOCTYPE html>
<html lang="en">
<head>
<meta charset="utf-8">
<title>VKTO Meridian LLC</title>
<link rel="stylesheet" href="https://fonts.googleapis.com/css2?family=Michroma&family=Noto+Sans:ital,wght@0,400;0,600;0,700;1,400&family=Roboto:ital,wght@0,400;0,700;1,400&display=swap">
<style>
:root{
  --red:#c8073d;
  --red-deep:#9d0f33;
  --navy:#0e1a33;
  --ink:#1a1a1a;
  --grey:#5b5b5b;
  --line:#dedede;
  --white:#ffffff;
  --black:#07070a;
}
*{box-sizing:border-box;margin:0;padding:0}
html,body{width:1200px;height:2809px;overflow:hidden}
body{position:relative;background:var(--white);font-family:"Noto Sans",sans-serif;color:var(--ink)}
.abs{position:absolute}

/* top bar + header */
.topbar{left:0;top:0;width:1200px;height:34px;background:var(--red);color:var(--white);font-size:14px}
.topbar .item{position:absolute;top:8px;display:flex;align-items:center;gap:8px}
.topbar .divider{position:absolute;left:992px;top:8px;width:1px;height:18px;background:rgba(255,255,255,.4)}
.header{left:0;top:34px;width:1200px;height:71px;background:var(--white)}
.brand{left:58px;top:22px;display:flex;align-items:center;gap:10px;font-family:"Michroma",sans-serif;font-size:20px;color:var(--red);letter-spacing:.04em;white-space:nowrap}
.brand-dot{width:14px;height:14px;border-radius:50%;background:var(--red)}
.nav{right:62px;top:28px;display:flex;gap:23px;font-size:12.5px;text-transform:uppercase}
.nav a{color:#222;text-decoration:none}
.nav a.active{color:var(--red);position:relative}
.nav a.active::after{content:"";position:absolute;left:20px;top:20px;width:36px;height:2px;background:var(--red);transform:rotate(-8deg)}

/* hero */
.hero-art{left:0;top:105px}
.hero-title{left:58px;top:296px;font-family:"Roboto",sans-serif;font-weight:700;font-size:66px;letter-spacing:-1px;color:var(--white);white-space:nowrap}
.hero-title span{color:var(--red)}
.hero-sub{left:62px;top:375px;font-family:"Roboto",sans-serif;font-size:19px;color:var(--red)}
.hero-text{left:62px;top:416px;width:450px;font-family:"Roboto",sans-serif;font-style:italic;font-size:15.5px;line-height:22px;color:var(--white)}
.btn{display:flex;align-items:center;justify-content:center;background:var(--red);color:var(--white);border-radius:30px;font-family:"Michroma",sans-serif;font-size:13px;letter-spacing:.08em;text-transform:uppercase}
.hero-btn{left:60px;top:479px;width:187px;height:41px}
.hero-photo{left:729px;top:362px;width:366px;height:366px;border-radius:50%;border:3px solid var(--red);background:radial-gradient(circle at 45% 40%,#fff6d8 0 4%,#6a7486 10%,#23324f 38%,#0b1426 62%,#3e6aa5 85%,#a9c6e6 100%)}

/* about */
.photo{border-radius:10px}
.about-photo-a{left:182px;top:855px;width:285px;height:285px;background:linear-gradient(180deg,#f1ecdd 0%,#4f5b72 30%,#1b2740 60%,#5d7fa8 100%)}
.about-photo-b{left:339px;top:1019px;width:240px;height:240px;background:linear-gradient(180deg,#7fa3c0 0%,#9cb8cf 55%,#55585d 75%,#8d8f92 100%)}
.about-badge{left:326px;top:1002px;width:110px;height:110px;border-radius:50%;background:var(--white);display:flex;align-items:center;justify-content:center;font-family:"Michroma",sans-serif;font-size:11px;color:var(--red);text-align:center;line-height:15px}
.kicker{font-size:15px;text-transform:uppercase;color:var(--red)}
.bar{width:3px;background:var(--red)}
.h2{font-family:"Michroma",sans-serif;font-size:31px;text-transform:uppercase;letter-spacing:.05em;color:var(--ink);white-space:nowrap}
.about-copy{left:687px;top:950px;width:395px;font-size:11.5px;line-height:19.5px;color:var(--grey)}
.about-copy p+p{margin-top:19px}
.ticks{left:687px;top:1142px;list-style:none;font-style:italic;font-size:14px;color:var(--red)}
.ticks li{display:flex;align-items:center;gap:17px;height:27px}
.ticks li::before{content:"";width:8px;height:8px;border:2px solid var(--red);border-radius:50%}
.about-btn{left:686px;top:1219px;width:187px;height:41px}

/* services */
.services{left:0;top:1338px;width:1200px;height:620px;background:linear-gradient(180deg,#c83360 0%,#c42452 45%,#b8153f 80%,#c0163f 100%)}
.card{width:464px;height:239px;border-radius:8px;background:rgba(110,12,38,.55);box-shadow:0 2px 10px rgba(0,0,0,.15);overflow:hidden}
.card-photo{position:absolute;left:0;top:0;width:225px;height:239px;border-radius:0 120px 120px 0/0 120px 120px 0}
.card-photo.jet{background:linear-gradient(180deg,#b9c2cc 0%,#d2c3a9 45%,#e0a66a 62%,#3e3f46 80%,#7a7b80 100%)}
.card-photo.station{background:linear-gradient(180deg,#05070d 0%,#1a2130 45%,#6c7a8e 70%,#c9d8ea 100%)}
.card-body{position:absolute;left:247px;top:45px;width:190px;color:#fff}
.card-title{font-family:"Michroma",sans-serif;font-size:17px;letter-spacing:.05em;line-height:20px;margin-bottom:12px}
.card-text{font-size:11.5px;line-height:19.5px}
.card-link{margin-top:14px;font-style:italic;font-size:12px;color:#a30a32;display:flex;align-items:center;gap:8px}

/* contact */
.contact-sub{left:136px;top:2008px;font-style:italic;font-size:14px;color:var(--grey)}
.info{left:120px;display:flex;gap:18px}
.info-icon{width:55px;height:55px;border-radius:50%;border:3px solid #f3c2cf;display:flex;align-items:center;justify-content:center;flex:none}
.info-icon i{width:42px;height:42px;border-radius:50% 50% 50% 8px;background:var(--red);display:flex;align-items:center;justify-content:center}
.info-name{font-weight:700;font-size:14px;margin-top:2px}
.info-text{font-size:12px;line-height:20px;color:var(--grey)}
.field{height:41px;border:1px solid var(--line);border-radius:8px;background:#fff;box-shadow:0 2px 5px rgba(0,0,0,.06);display:flex;align-items:center;gap:12px;padding-left:12px;font-size:12px;color:#666}
.field.message{align-items:flex-start;padding-top:10px;height:90px}
.submit{left:507px;top:2306px;width:127px;height:41px}

/* footer */
.footer-art{left:0;top:2400px}
.foot-brand{left:74px;top:2616px;width:226px;font-family:"Michroma",sans-serif;font-size:17px;color:#fff;letter-spacing:.03em;white-space:nowrap}
.social{left:124px;top:2686px;display:flex;gap:8px}
.social span{width:38px;height:38px;border-radius:50%;border:2px solid var(--red)}
.foot-head{font-family:"Michroma",sans-serif;font-size:14px;color:var(--red);text-transform:uppercase;letter-spacing:.06em}
.sitemap{left:343px;top:2605px;list-style:none;color:#fff;font-size:12px}
.sitemap li{display:flex;align-items:center;gap:12px;height:24px}
.sitemap li::before{content:"";width:6px;height:6px;border:1.5px solid var(--red);border-radius:50%}
.foot-contact{left:588px;color:#fff;font-size:12px;line-height:19px;display:flex;gap:16px;align-items:flex-start}
.news-input{left:879px;top:2617px;width:252px;height:41px;border-radius:8px;background:#fff;font-size:12px;color:#666;display:flex;align-items:center;padding-left:18px}
.news-btn{left:879px;top:2670px;width:164px;height:41px}
.foot-line{left:0;top:2765px;width:1200px;height:1px;background:rgba(255,255,255,.12)}
.copyright{left:0;top:2775px;width:1200px;text-align:center;color:#fff;font-size:12px}
.copyright span{color:var(--red)}
</style>
</head>
<body>

<!-- top bar -->
<div class="abs topbar">
  <div class="item" style="left:818px">
    <svg width="20" height="16" viewBox="0 0 20 16" fill="none" stroke="#fff" stroke-width="1.5"><rect x="1" y="1" width="18" height="14" rx="1"/><path d="M1 2l9 7 9-7M1 15l7-6M19 15l-7-6"/></svg>
    info@vktomeridian.com
  </div>
  <div class="divider"></div>
  <div class="item" style="left:1013px;font-weight:700;font-size:15px">
    <svg width="20" height="20" viewBox="0 0 24 24" fill="none" stroke="#fff" stroke-width="1.5"><path d="M5 2h4l2 5-3 2a11 11 0 0 0 7 7l2-3 5 2v4a2 2 0 0 1-2 2A19 19 0 0 1 3 4a2 2 0 0 1 2-2z"/></svg>
    123.456.7890
  </div>
</div>

<header class="abs header">
  <div class="abs brand"><span class="brand-dot"></span>VKTO MERIDIAN</div>
  <nav class="abs nav">
    <a class="active" href="#">Home</a><a href="#">About</a><a href="#">Services</a><a href="#">Contact Us</a>
  </nav>
</header>

<!-- hero -->
<svg class="abs hero-art" width="1200" height="680" viewBox="0 0 1200 680">
  <defs>
    <linearGradient id="space" x1="0" y1="0" x2="1" y2="1">
      <stop offset="0" stop-color="#2d4a6c"/>
      <stop offset=".35" stop-color="#13233f"/>
      <stop offset="1" stop-color="#0b1428"/>
    </linearGradient>
  </defs>
  <path d="M0 0H1200V233C1020 370 760 560 420 645C250 680 100 655 0 620Z" fill="#c8073d"/>
  <path role="img" aria-label="Earth from orbit with a space shuttle launching" d="M0 0H1200V276C1020 405 760 565 420 602C250 622 100 608 0 588Z" fill="url(#space)"/>
</svg>
<div class="abs hero-title"><span>VKTO</span>MERIDIAN</div>
<div class="abs hero-sub">Defense And Federal Space Experts</div>
<div class="abs hero-text">Lorem Ipsum has been the industry's standard dummy text ever since the 1500s, when an unknown printer took.</div>
<div class="abs btn hero-btn">Contact Us</div>
<div class="abs hero-photo" role="img" aria-label="Satellite orbiting above Earth"></div>

<!-- about -->
<div class="abs photo about-photo-a" role="img" aria-label="Space station above Earth"></div>
<div class="abs photo about-photo-b" role="img" aria-label="Fighter jet landing on a carrier deck"></div>
<div class="abs about-badge">VKTO<br>MERIDIAN</div>

<div class="abs bar" style="left:673px;top:872px;height:54px"></div>
<div class="abs kicker" style="left:688px;top:870px">Welcome To</div>
<div class="abs h2" style="left:685px;top:898px">VKTO Meridian</div>
<div class="abs about-copy">
  <p>Lorem Ipsum has been the industry's standard dummy text ever since the 1500s, when an unknown printer took a galley of type and scrambled it to make a type specimen book.</p>
  <p>Lorem Ipsum has been the industry's standard dummy text ever since the 1500s, when an unknown printer took a galley of type &amp; scrambled it to make a type specimen book. It has survived not only five centuries, but also the leap into electronic typesetting, remaining essentially unch. has been the industry's standard dummy text ever since..</p>
</div>
<ul class="abs ticks">
  <li>Lorem Ipsum has been the industry's standard dummy</li>
  <li>Lorem Ipsum has been the industry's standard dummy</li>
</ul>
<div class="abs btn about-btn">Learn More</div>

<!-- services -->
<section class="abs services" role="img" aria-label="Red tinted fighter jet background"></section>
<div class="abs bar" style="left:120px;top:1413px;height:55px;background:#3a0a16"></div>
<div class="abs kicker" style="left:135px;top:1412px;color:#1a1a1a">What We Do</div>
<div class="abs h2" style="left:132px;top:1437px;color:#fff">Services</div>

<div class="abs card" style="left:120px;top:1507px">
  <div class="card-photo jet" role="img" aria-label="Fighter jet on a carrier at sunset"></div>
  <div class="card-body">
    <div class="card-title">DEFENCE</div>
    <div class="card-text">Lorem Ipsum has been the industry's standard dummy text ever since the when an unknown printer took a galley...</div>
    <div class="card-link">Learn More <svg width="18" height="8" viewBox="0 0 18 8"><path d="M0 4H15" stroke="#a30a32"/><path d="M13 0l5 4-5 4z" fill="#a30a32"/></svg></div>
  </div>
</div>
<div class="abs card" style="left:615px;top:1507px">
  <div class="card-photo station" role="img" aria-label="Space station above Earth"></div>
  <div class="card-body">
    <div class="card-title">FEDERAL<br>SPACE</div>
    <div class="card-text">Lorem Ipsum has been the industry's standard dummy text ever since the when an type..</div>
    <div class="card-link">Learn More <svg width="18" height="8" viewBox="0 0 18 8"><path d="M0 4H15" stroke="#a30a32"/><path d="M13 0l5 4-5 4z" fill="#a30a32"/></svg></div>
  </div>
</div>

<svg class="abs" style="left:0;top:1780px" width="1200" height="190" viewBox="0 1780 1200 190">
  <path d="M0 1934C120 1850 250 1812 400 1814L400 1826C260 1826 150 1860 0 1945Z" fill="#1b1b22"/>
  <path d="M0 1945C150 1860 260 1826 400 1826C600 1826 750 1920 900 1918C1050 1916 1150 1870 1200 1850V1970H0Z" fill="#fff"/>
</svg>

<!-- contact -->
<div class="abs bar" style="left:120px;top:1938px;height:54px"></div>
<div class="abs kicker" style="left:135px;top:1936px">Keep In Touch</div>
<div class="abs h2" style="left:132px;top:1961px;font-size:33px">Contact Us</div>
<div class="abs contact-sub">If you have an any Question for contact Us Today !</div>

<div class="abs info" style="top:2082px">
  <div class="info-icon"><i><svg width="18" height="20" viewBox="0 0 18 22" fill="none" stroke="#fff" stroke-width="1.6"><path d="M9 21s-7-7-7-12a7 7 0 0 1 14 0c0 5-7 12-7 12z"/><circle cx="9" cy="9" r="2.5"/></svg></i></div>
  <div><div class="info-name">VKTO MERIDIAN</div><div class="info-text">101 - Address City Sate Office<br>street. pincode</div></div>
</div>
<div class="abs info" style="top:2158px">
  <div class="info-icon"><i><svg width="18" height="18" viewBox="0 0 24 24" fill="none" stroke="#fff" stroke-width="1.8"><path d="M5 2h4l2 5-3 2a11 11 0 0 0 7 7l2-3 5 2v4a2 2 0 0 1-2 2A19 19 0 0 1 3 4a2 2 0 0 1 2-2z"/></svg></i></div>
  <div><div class="info-name">Phone</div><div class="info-text" style="font-size:13px">123. 456 .7890</div></div>
</div>
<div class="abs info" style="top:2234px">
  <div class="info-icon"><i><svg width="18" height="14" viewBox="0 0 20 16" fill="none" stroke="#fff" stroke-width="1.6"><rect x="1" y="1" width="18" height="14" rx="1"/><path d="M1 2l9 7 9-7M1 15l7-6M19 15l-7-6"/></svg></i></div>
  <div><div class="info-name">Email</div><div class="info-text">info@VktoMeridian.Com</div></div>
</div>

<div class="abs field" style="left:507px;top:2084px;width:269px">
  <svg width="20" height="20" viewBox="0 0 20 20" fill="none" stroke="#c8073d" stroke-width="1.4"><circle cx="10" cy="10" r="9"/><circle cx="10" cy="8" r="3"/><path d="M4 16c2-3 10-3 12 0"/></svg>Name
</div>
<div class="abs field" style="left:796px;top:2084px;width:269px">
  <svg width="20" height="16" viewBox="0 0 20 16" fill="none" stroke="#333" stroke-width="1.4"><rect x="1" y="1" width="18" height="14" rx="1"/><path d="M1 2l9 7 9-7M1 15l7-6M19 15l-7-6"/></svg>Email
</div>
<div class="abs field" style="left:507px;top:2144px;width:269px">
  <svg width="20" height="20" viewBox="0 0 24 24" fill="none" stroke="#333" stroke-width="1.4"><path d="M5 2h4l2 5-3 2a11 11 0 0 0 7 7l2-3 5 2v4a2 2 0 0 1-2 2A19 19 0 0 1 3 4a2 2 0 0 1 2-2z"/></svg>Phone
</div>
<div class="abs field" style="left:796px;top:2144px;width:269px;padding-left:14px">Services
  <svg style="position:absolute;right:12px;top:18px" width="10" height="6" viewBox="0 0 10 6"><path d="M0 0h10L5 6z" fill="#333"/></svg>
</div>
<div class="abs field message" style="left:507px;top:2200px;width:558px">
  <svg width="20" height="18" viewBox="0 0 20 18" fill="none" stroke="#333" stroke-width="1.4"><path d="M2 2h16v11H8l-4 4v-4H2z"/><circle cx="6.5" cy="7.5" r=".8" fill="#333"/><circle cx="10" cy="7.5" r=".8" fill="#333"/><circle cx="13.5" cy="7.5" r=".8" fill="#333"/></svg>Message
</div>
<div class="abs btn submit">Submit</div>

<!-- footer -->
<svg class="abs footer-art" width="1200" height="409" viewBox="0 2400 1200 409">
  <defs>
    <linearGradient id="night" x1="0" y1="0" x2="0" y2="1">
      <stop offset="0" stop-color="#141418"/>
      <stop offset=".6" stop-color="#08080b"/>
      <stop offset="1" stop-color="#101520"/>
    </linearGradient>
  </defs>
  <path d="M0 2562C300 2470 680 2418 960 2422C1110 2426 1190 2540 1200 2640V2809H0Z" fill="#c8073d"/>
  <path role="img" aria-label="Dark view of a space station against the night sky" d="M0 2575C300 2505 680 2470 930 2480C1080 2490 1170 2580 1200 2690V2809H0Z" fill="url(#night)"/>
</svg>
<div class="abs foot-brand">VKTO MERIDIAN</div>
<div class="abs social"><span></span><span></span><span></span></div>

<div class="abs foot-head" style="left:343px;top:2570px">Sitemap</div>
<ul class="abs sitemap">
  <li>Home</li><li>About</li><li>Services</li><li>Contact</li>
</ul>

<div class="abs foot-head" style="left:590px;top:2570px">Contact Us</div>
<div class="abs foot-contact" style="top:2608px">
  <svg width="20" height="24" viewBox="0 0 18 22" fill="none" stroke="#c8073d" stroke-width="1.4"><path d="M9 21s-7-7-7-12a7 7 0 0 1 14 0c0 5-7 12-7 12z"/><circle cx="9" cy="9" r="2.5"/></svg>
  <div>101 - Address City Sate Office<br>street. pincode</div>
</div>
<div class="abs foot-contact" style="top:2661px">
  <svg width="20" height="20" viewBox="0 0 24 24" fill="none" stroke="#c8073d" stroke-width="1.4"><path d="M5 2h4l2 5-3 2a11 11 0 0 0 7 7l2-3 5 2v4a2 2 0 0 1-2 2A19 19 0 0 1 3 4a2 2 0 0 1 2-2z"/></svg>
  <div style="font-size:13px">123. 456 .7890</div>
</div>
<div class="abs foot-contact" style="top:2697px">
  <svg width="20" height="16" viewBox="0 0 20 16" fill="none" stroke="#c8073d" stroke-width="1.4"><rect x="1" y="1" width="18" height="14" rx="1"/><path d="M1 2l9 7 9-7M1 15l7-6M19 15l-7-6"/></svg>
  <div>info@VktoMeridian.Com</div>
</div>

<div class="abs foot-head" style="left:880px;top:2570px">Newsletter !</div>
<div class="abs news-input">Enter Email *</div>
<div class="abs btn news-btn">Subscribe</div>

<div class="abs foot-line"></div>
<div class="abs copyright">©<span>VKTO MERIDIAN</span> -2022 All rights reserved.</div>

</body>
</html>
```